Trelan - The first sidebot ever!

We need 2 banners design (300X600 and 300X250) for the launch campaign of a new product/brand called Trelan. Trelan is a sidebot - part of a new class of industrial robots designed t work safely and efficiently alongside humans.
Find the landing page here: https://thetrelan.example/
The main objective is to create awareness about the product launch and secondly increase website traffic. You may want to propose a meaningful CTA to ensure meeting those objectives.
Also, all useful guidelines attached as well as its basic assets. You can ask me for UI elements if needed. Also, you have the video script that may go with the display banners if that helps.

Target Market(s)

Geo targeting: Europe, USA
Target groups: 1 - CXO, Directors, Managers and Owners of Industrial Manufacturing Industries of all sizes;
2 - Engineers machine integrators who are selling and integrating our product in their solutions to Industrial people (target 1)
3 - Industrial equipment resellers.

Industry/Entity Type

Industry

Font styles to use
Sans Serif

Requirements
Must have
• Logo, at least one of the photos provided, CTA, and colors, and fonts as described in the UI guidelines provided (for this reason I am not picking colors in the disc provided here)
Nice to have
• HTML5 or GIF animation (minimalist style).
Should not have
• Too much text or too charged design

```html
<!DOCTYPE html>
<html lang="en">
<head>
<meta charset="UTF-8">
<title>Trelan — Ready to get started?</title>
<link href="https://fonts.googleapis.com/css2?family=Quicksand:wght@500;600;700&family=Montserrat:wght@500;600;700&display=swap" rel="stylesheet">
<style>
  :root {
    --bg-dark: #1b1e27;
    --accent-red: #ef1a3c;
    --text-light: #ffffff;
    --footer-bg: #ffffff;
    --logo-ink: #1b1e27;
    --photo-tone-a: #d9dbe0;
    --photo-tone-b: #8f949c;
  }
  * { margin: 0; padding: 0; box-sizing: border-box; }
  html, body { width: 1200px; height: 2400px; overflow: hidden; background: var(--bg-dark); }
  .banner {
    position: relative;
    width: 1200px;
    height: 2400px;
    background: var(--bg-dark);
    overflow: hidden;
  }
  .banner-shapes { position: absolute; inset: 0; width: 1200px; height: 2400px; }
  .headline {
    position: absolute;
    left: 184px;
    top: 300px;
    width: 900px;
    font-family: "Quicksand", sans-serif;
    font-weight: 600;
    font-size: 104px;
    line-height: 112px;
    color: var(--text-light);
    letter-spacing: 2px;
  }
  .intro-copy {
    position: absolute;
    left: 184px;
    top: 590px;
    width: 820px;
    font-family: "Montserrat", sans-serif;
    font-weight: 500;
    font-size: 48px;
    line-height: 80px;
    color: var(--text-light);
  }
  .cta-button {
    position: absolute;
    left: 184px;
    top: 930px;
    height: 92px;
    padding: 0 48px;
    display: flex;
    align-items: center;
    gap: 20px;
    border-radius: 46px;
    background: var(--accent-red);
    color: var(--text-light);
    font-family: "Montserrat", sans-serif;
    font-weight: 700;
    font-size: 40px;
    letter-spacing: 1px;
    text-decoration: none;
  }
  .cta-arrow { width: 36px; height: 36px; }
  .brand-footer {
    position: absolute;
    left: 0;
    top: 2080px;
    width: 1200px;
    height: 320px;
    background: var(--footer-bg);
    display: flex;
    align-items: center;
    justify-content: center;
  }
  .brand-name {
    font-family: "Quicksand", sans-serif;
    font-weight: 600;
    font-size: 104px;
    letter-spacing: 10px;
    color: var(--logo-ink);
    text-transform: uppercase;
  }
</style>
</head>
<body>
<main class="banner">
  <svg class="banner-shapes" viewBox="0 0 1200 2400" xmlns="http://www.w3.org/2000/svg">
    <defs>
      <linearGradient id="photoTone" x1="0" y1="0" x2="1" y2="1">
        <stop offset="0" stop-color="#d9dbe0"/>
        <stop offset="1" stop-color="#8f949c"/>
      </linearGradient>
      <clipPath id="aboveFooter"><rect x="0" y="0" width="1200" height="2080"/></clipPath>
    </defs>

    <g class="flow-lines" fill="none" stroke="#ffffff" stroke-width="4" opacity="0.85">
      <path d="M0 330 C120 380 110 560 40 700 C-20 820 60 960 180 1040 C300 1120 260 1240 200 1320 C140 1420 260 1500 320 1560"/>
      <path d="M1200 480 C1080 560 1130 720 1060 860 C990 1000 1120 1080 1040 1200 C960 1320 1010 1420 1120 1460"/>
      <path d="M0 1640 C140 1560 260 1620 300 1700"/>
    </g>

    <circle class="accent-dot" cx="180" cy="160" r="180" fill="#ef1a3c"/>
    <circle class="accent-ring" cx="960" cy="40" r="150" fill="none" stroke="#ef1a3c" stroke-width="50"/>

    <path class="cross-outline" d="M420 1062 L460 1102 L500 1062 L540 1102 L500 1142 L540 1182 L500 1222 L460 1182 L420 1222 L380 1182 L420 1142 L380 1102 Z" fill="none" stroke="#ef1a3c" stroke-width="14"/>
    <path class="cross-solid" d="M1090 970 L1140 1020 L1190 970 L1240 1020 L1190 1070 L1240 1120 L1190 1170 L1140 1120 L1090 1170 L1040 1120 L1090 1070 L1040 1020 Z" fill="#ef1a3c"/>

    <g clip-path="url(#aboveFooter)">
      <circle class="frame-ring" cx="600" cy="1880" r="500" fill="none" stroke="#ef1a3c" stroke-width="80"/>
      <circle class="product-photo" cx="600" cy="1880" r="452" fill="url(#photoTone)" role="img" aria-label="Photo of a worker operating the Trelan sidebot's touchscreen panel beside a white industrial robot arm"/>
    </g>
  </svg>

  <h1 class="headline">Ready to get<br>started?</h1>
  <p class="intro-copy">Meet the first sidebot: a new class of industrial robot built to work safely side by side with your team.</p>

  <a class="cta-button" href="https://thetrelan.example/">
    Discover Trelan
    <svg class="cta-arrow" viewBox="0 0 24 24" fill="none" stroke="#ffffff" stroke-width="3" stroke-linecap="round" stroke-linejoin="round" aria-hidden="true"><path d="M4 12 H19 M13 6 L19 12 L13 18"/></svg>
  </a>

  <footer class="brand-footer">
    <span class="brand-name">Trelan</span>
  </footer>
</main>
</body>
</html>
```